Parcel Craze Weekly needs 2 graphic placements for our home page

parcelcrazeweekly.net's home page has two featured image placements for "Coupons & Deals" and "The Best Beauty Boxes". We'd like to change those graphics to something more creative and on brand.

Image requirements: 234px x 150px.

We'd like the text to be integrated into the graphic design, and it does not have to be on top like the images that were uploaded

The images your work will replace are attached.

Target Market(s)

We do not want to lean towards any gender

Industry/Entity Type

Graphic Design

Font styles to use
Sans Serif

Requirements
Must have
• 234px x 150px.

```html
<!DOCTYPE html>
<html lang="en">
<head>
<meta charset="utf-8">
<title>Parcel Craze Weekly – home page placements</title>
<link rel="stylesheet" href="https://fonts.googleapis.com/css2?family=Arvo:wght@700&family=Bodoni+Moda:wght@500&family=Questrial&display=swap">
<style>
  :root {
    --sheet: #f1f1f1;
    --sheet-glow: #ffffff;
    --ink: #000000;
    --paper: #ffffff;
    --teal: #2b7f80;
    --teal-deep: #1d5f63;
    --teal-light: #5fc1c3;
    --magenta: #b3166c;
    --magenta-deep: #8e0f55;
    --pink: #cf4d96;
    --beige: #d9cfc6;
    --mist: #e9e9ea;
    --photo-bags: #3b4658;
    --photo-beauty: #e3d3da;
    --caption: #ffffff;
  }
  * { box-sizing: border-box; margin: 0; padding: 0; }
  html, body { width: 1200px; height: 848px; overflow: hidden; }
  body {
    position: relative;
    background: radial-gradient(ellipse at 55% 20%, var(--sheet-glow) 0%, var(--sheet) 70%, #e6e6e6 100%);
    font-family: "Questrial", sans-serif;
  }
  .corner-band { position: absolute; left: 0; top: 0; width: 240px; height: 110px; }
  .placement {
    position: absolute;
    border: 4px solid var(--paper);
    background: var(--paper);
    box-shadow: 2px 4px 8px rgba(0,0,0,.35);
    overflow: hidden;
  }
  .placement svg { display: block; width: 100%; height: 100%; }
  .placement--coupons { left: 131px; top: 226px; width: 480px; height: 307px; }
  .placement--beauty { left: 587px; top: 359px; width: 481px; height: 308px; }
  .headline-slab { font-family: "Arvo", serif; font-weight: 700; fill: var(--paper); }
  .headline-serif { font-family: "Bodoni Moda", serif; font-weight: 500; fill: var(--paper); }
  .dot-rule { stroke: var(--paper); stroke-width: 6; stroke-dasharray: 6 5; }
  .footer-bar {
    position: absolute; left: 0; bottom: 0; width: 1200px; height: 56px;
    background: var(--ink);
  }
  .footer-caption {
    position: absolute; left: 64px; top: 18px;
    color: var(--caption); font-size: 15px;
  }
</style>
</head>
<body>
  <svg class="corner-band" viewBox="0 0 240 110" aria-hidden="true">
    <polygon points="0,0 226,0 0,102" fill="var(--ink)"/>
  </svg>

  <div class="placement placement--coupons">
    <svg viewBox="0 0 472 299">
      <defs>
        <radialGradient id="tealPanel" cx="50%" cy="40%" r="70%">
          <stop offset="0" stop-color="var(--teal)"/>
          <stop offset="1" stop-color="var(--teal-deep)"/>
        </radialGradient>
      </defs>
      <rect width="472" height="299" fill="var(--beige)"/>
      <path d="M10 38 Q8 28 22 30 L330 66 Q350 70 350 90 L345 268 Q344 290 322 290 L40 290 Q16 290 14 266 Z" fill="var(--magenta)"/>
      <path d="M24 0 L472 0 L472 242 Q472 256 458 256 L120 256 Q28 256 24 170 Z" fill="url(#tealPanel)"/>
      <g transform="rotate(-5 236 150)">
        <line class="dot-rule" x1="120" y1="40" x2="340" y2="40"/>
        <text class="headline-slab" x="45" y="112" font-size="68">Coupons</text>
        <line class="dot-rule" x1="255" y1="134" x2="365" y2="134"/>
        <line class="dot-rule" x1="60" y1="150" x2="165" y2="150"/>
        <text class="headline-slab" x="175" y="200" font-size="70">&amp;Deals</text>
        <line class="dot-rule" x1="265" y1="220" x2="430" y2="220"/>
      </g>
      <rect x="20" y="180" width="150" height="92" rx="6" fill="var(--photo-bags)" role="img" aria-label="Photo of two shopping bags spilling clipped coupons"/>
    </svg>
  </div>

  <div class="placement placement--beauty">
    <svg viewBox="0 0 473 300">
      <defs>
        <linearGradient id="mist" x1="0" y1="0" x2="0" y2="1">
          <stop offset="0" stop-color="#f4f4f5"/>
          <stop offset="1" stop-color="var(--mist)"/>
        </linearGradient>
        <radialGradient id="shield" cx="50%" cy="40%" r="65%">
          <stop offset="0" stop-color="var(--pink)"/>
          <stop offset="1" stop-color="var(--magenta-deep)"/>
        </radialGradient>
      </defs>
      <rect width="473" height="300" fill="url(#mist)"/>
      <rect width="473" height="48" fill="var(--teal-light)"/>
      <path d="M24 0 L449 0 Q462 62 420 92 Q330 150 237 150 Q144 150 54 92 Q12 62 24 0 Z" fill="url(#shield)"/>
      <path d="M0 168 Q80 150 150 175" fill="none" stroke="var(--magenta)" stroke-width="4"/>
      <path d="M323 175 Q400 150 473 168" fill="none" stroke="var(--magenta)" stroke-width="4"/>
      <text class="headline-serif" x="236" y="52" font-size="38" text-anchor="middle">The Best</text>
      <text class="headline-serif" x="236" y="100" font-size="38" text-anchor="middle">Beauty Boxes</text>
      <rect x="82" y="156" width="310" height="134" rx="6" fill="var(--photo-beauty)" role="img" aria-label="Photo of a gift box surrounded by beauty products"/>
    </svg>
  </div>

  <div class="footer-bar">
    <p class="footer-caption">Parcel Craze Weekly 2 graphic placements for home page</p>
  </div>
</body>
</html>
```